"Harrow Crest Builders" is a residential building company and needs a new business card design and may re

We would like a redesign based on the existing logo, and would like to see a new font as well. We are bespoke home builders who build sustainable energy efficient homes.

Industry/Entity Type

Construction

Contact Information for Business Card

Business card size 40mm x 90mm

Colors

Designer to choose colors to be used in the design.

```html
<!DOCTYPE html>
<html lang="en">
<head>
<meta charset="utf-8">
<title>Harrow Crest Builders – Business Card</title>
<link href="https://fonts.googleapis.com/css2?family=Exo+2:wght@400;500&display=swap" rel="stylesheet">
<style>
  :root {
    --backdrop: #2e2e2e;
    --card: #0b0b0b;
    --card-edge: #1a1a1a;
    --lime: #b9d530;
    --ink: #ffffff;
    --ink-soft: #e6e6e6;
    --badge: #ffffff;
    --shade: #151515;
  }
  * { box-sizing: border-box; margin: 0; padding: 0; }
  html, body {
    width: 1200px; height: 900px; overflow: hidden;
    background: var(--backdrop);
    font-family: "Exo 2", sans-serif;
    color: var(--ink);
  }
  .canvas { position: relative; width: 1200px; height: 900px; }
  .card {
    position: absolute;
    width: 580px; height: 340px;
    background: var(--card);
    border-radius: 22px;
    border: 1px solid var(--card-edge);
    overflow: hidden;
    box-shadow: 0 18px 40px rgba(0,0,0,.55);
  }
  /* Logo side */
  .card--brand { left: 560px; top: 70px; }
  .card--brand .shade-band {
    position: absolute; right: -40px; top: 40px;
    width: 300px; height: 260px;
    background: var(--shade);
    transform: skewX(-18deg);
  }
  .brand-lockup {
    position: absolute; left: 70px; top: 110px;
    display: flex; align-items: center; gap: 18px;
  }
  .brand-lockup .brand-square {
    width: 34px; height: 34px; background: var(--lime);
  }
  .brand-name {
    font-weight: 400; font-size: 40px; letter-spacing: 1px;
    color: var(--ink); line-height: 1;
  }
  .brand-url {
    position: absolute; left: 122px; top: 190px;
    font-size: 17px; letter-spacing: 2px; color: var(--ink-soft);
  }
  /* Contact side */
  .card--contact { left: 80px; top: 470px; }
  .contact-band { position: absolute; inset: 0; }
  .holder-name {
    position: absolute; left: 40px; top: 34px;
    font-size: 30px; font-weight: 500; letter-spacing: 1px;
  }
  .contact-list {
    position: absolute; left: 40px; top: 118px;
    list-style: none; font-size: 16px; line-height: 27px;
  }
  .contact-list li { display: flex; align-items: center; gap: 10px; }
  .contact-list svg { width: 18px; height: 18px; flex: none; }
  .contact-list .no-icon { padding-left: 0; }
  .legal-line { font-size: 16px; }
  .member-badge {
    position: absolute; right: 60px; bottom: 34px;
    width: 130px; height: 78px; background: var(--badge);
  }
</style>
</head>
<body>
<main class="canvas">

  <section class="card card--brand" aria-label="Business card, logo side">
    <div class="shade-band"></div>
    <div class="brand-lockup">
      <span class="brand-square"></span>
      <span class="brand-name">Harrow Crest Builders</span>
    </div>
    <p class="brand-url">www.harrowcrestbuilders.com.au</p>
  </section>

  <section class="card card--contact" aria-label="Business card, contact side">
    <svg class="contact-band" viewBox="0 0 580 340" preserveAspectRatio="none" aria-hidden="true">
      <polygon points="340,0 580,0 580,96 520,96" fill="#151515"/>
      <polygon points="372,0 412,0 522,96 580,96 580,128 506,128" fill="var(--lime)"/>
      <polygon points="450,150 580,150 580,190 480,190" fill="#131313"/>
    </svg>
    <h1 class="holder-name">Daniel Marchetti</h1>
    <ul class="contact-list">
      <li>
        <svg viewBox="0 0 20 20" aria-hidden="true"><path fill="var(--lime)" d="M5 2l3 3-2 3c1 2 3 4 5 5l2-2 3 3-2 3C8 17 3 12 2 5z"/></svg>
        <span>0400 318 776</span>
      </li>
      <li>
        <svg viewBox="0 0 20 20" aria-hidden="true"><rect x="2" y="4" width="16" height="12" fill="var(--lime)"/><path d="M2 4l8 7 8-7" fill="none" stroke="#0b0b0b" stroke-width="1.5"/></svg>
        <span>daniel@harrowcrestbuilders.com.au</span>
      </li>
      <li>
        <svg viewBox="0 0 20 20" aria-hidden="true"><g fill="none" stroke="var(--lime)" stroke-width="1.6"><circle cx="10" cy="10" r="8"/><ellipse cx="10" cy="10" rx="3.5" ry="8"/><path d="M2 10h16M4 5.5h12M4 14.5h12"/></g></svg>
        <span>www.harrowcrestbuilders.com.au</span>
      </li>
      <li class="legal-line">PO Box 2174 Eastgate LPO Hallsworth WA 6099</li>
      <li class="legal-line">Registration 40872 &nbsp;|&nbsp; ABN: 53 208 614 397</li>
    </ul>
    <div class="member-badge" role="img" aria-label="Industry association membership badge"></div>
  </section>

</main>
</body>
</html>
```